Design a simple and clean PowerPoint slide templates for a Board meeting. The slides should have predominantly white backgrounds and use the brand graphic standards (attached). I'm also attached a PowerPoint master that I don't like, as it's too basic.
The company name is Harborline Weighworks.
It sells, calibrates, services and repairs industrial and commercial scales of all types. In particular, Truck scales, floor scales, counting scales and benchtop scales.
The website is harborlineweighworks.example but this are the old colors, so ignore the logo and colors. We are launching a new logo and new look. Several variations of the logo are available.

```html
<!DOCTYPE html>
<html lang="en">
<head>
<meta charset="utf-8">
<title>Harborline Weighworks – Board Meeting Slide Templates</title>
<link href="https://fonts.googleapis.com/css2?family=Roboto:ital,wght@0,400;0,500;0,700;1,400&display=swap" rel="stylesheet">
<style>
:root{
  --navy:#1c355e;
  --orange:#f7941d;
  --orange-deep:#e8702a;
  --blue:#1aa3dc;
  --teal:#1d5a7e;
  --green:#1c6e2f;
  --pill:#eceff2;
  --ink:#222;
  --muted:#555;
  --stage:#d6d6d6;
  --faint:#f4f5f7;
}
*{box-sizing:border-box;margin:0;padding:0}
html,body{width:1200px;height:1119px;overflow:hidden}
body{background:var(--stage);font-family:'Roboto',Arial,sans-serif;position:relative;color:var(--ink)}
.slide{position:absolute;width:514px;height:289px;background:#fff;overflow:hidden;box-shadow:0 4px 10px rgba(0,0,0,.25)}
.s-cover{left:69px;top:79px}
.s-agenda{left:620px;top:79px}
.s-donut{left:69px;top:427px}
.s-text{left:620px;top:427px}
.s-process{left:69px;top:761px}
.s-close{left:620px;top:761px}
.abs{position:absolute}
.frame{position:absolute;left:0;top:0;width:514px;height:289px}
.slide-title{position:absolute;left:19px;top:18px;font-size:11.6px;font-weight:700;color:var(--navy);white-space:nowrap}
.brand-mini{position:absolute;right:14px;top:18px;width:60px;text-align:right;font-size:6px;line-height:7px;font-weight:700;color:var(--orange)}
.footnote{position:absolute;left:19px;top:276px;font-size:3.8px;color:#333;white-space:nowrap}
.page-no{position:absolute;left:430px;top:279px;font-size:5px;color:#fff}

/* cover */
.cover-photo{position:absolute;left:0;top:0;width:495px;height:289px;background:linear-gradient(120deg,#a27459 0%,#7b6a70 35%,#4d5876 65%,#5e6a85 100%)}
.cover-band{position:absolute;right:0;top:0;width:19px;height:289px;background:var(--orange)}
.sq{position:absolute}
.brand-cover{position:absolute;left:353px;top:36px;font-size:12px;line-height:13px;font-weight:700;color:#fff;letter-spacing:.5px}
.cover-title{position:absolute;left:266px;top:81px;width:217px;height:97px;background:rgba(38,52,92,.82);border-radius:10px 0 0 0;padding:18px 12px 0 25px;color:#fff;font-size:17px;line-height:20.5px;font-weight:700}
.cover-sub{position:absolute;left:266px;top:191px;width:217px;height:52px;background:rgba(38,52,92,.78);border-radius:8px 0 0 0;padding:10px 10px 0 22px;color:#fff;font-size:8.6px;line-height:10.4px;font-style:italic}
.cover-url{position:absolute;left:136px;top:246px;width:129px;height:23px;background:var(--orange-deep);border-radius:6px 0 0 0;color:#fff;font-size:8.4px;line-height:23px;text-align:center}

/* agenda */
.item{position:absolute;width:187px;height:27px;background:var(--pill)}
.item .num{position:absolute;left:0;top:0;width:25px;height:27px;background:var(--blue);clip-path:polygon(0 0,80% 0,100% 50%,80% 100%,0 100%);color:#fff;font-size:10px;font-weight:700;line-height:27px;padding-left:3px}
.item .head{position:absolute;left:33px;top:5px;font-size:7.3px;font-weight:700;color:var(--navy)}
.item .sub{position:absolute;left:33px;top:16px;font-size:6px;color:var(--muted)}

/* donut */
.pill{position:absolute;height:36px;width:160px;background:var(--pill);border-radius:18px}
.pill-text{position:absolute;font-size:5.7px;line-height:7.3px;color:#333;width:98px}
.dot{position:absolute;width:35px;height:35px;border-radius:50%}
.donut-label{position:absolute;left:205px;top:146px;width:80px;text-align:center;font-size:7.5px;line-height:9.5px;color:#444}

/* text slide */
.body-copy{position:absolute;left:45px;top:88px;width:188px;font-size:6.6px;line-height:8.75px;text-align:justify;color:#111}
.photo-caliper{position:absolute;left:270px;top:87px;width:191px;height:132px;border-radius:0 0 18px 0;background:linear-gradient(135deg,#1b3350 0%,#33577d 45%,#8fa3b8 60%,#27425f 100%)}

/* process */
.step-title{position:absolute;width:100px;text-align:center;font-size:7px;font-weight:700;color:#222}
.step-text{position:absolute;width:100px;text-align:center;font-size:5.3px;line-height:6.8px;color:#333}

/* closing */
.close-left{position:absolute;left:0;top:0;width:204px;height:289px;background:var(--navy)}
.close-photo{position:absolute;left:204px;top:0;width:310px;height:289px;background:linear-gradient(135deg,#c9d7ea 0%,#b3c6e0 45%,#dfe8f3 100%)}
.brand-close{position:absolute;left:30px;top:40px;font-size:12px;line-height:13px;font-weight:700;color:#fff;letter-spacing:.5px}
.cta{position:absolute;left:31px;top:125px;width:191px;height:132px;background:var(--orange);clip-path:polygon(26px 0,100% 0,100% 100%,0 100%,0 26px)}
.cta-head{position:absolute;left:29px;top:24px;color:#fff;font-size:15px;line-height:24px}
.cta-link{position:absolute;left:29px;font-size:6.4px;color:#fff}
.thanks{position:absolute;left:240px;top:128px;width:240px;text-align:center;color:#fff;font-size:29px;font-weight:700}
</style>
</head>
<body>

<!-- Cover -->
<section class="slide s-cover">
  <div class="cover-photo" role="img" aria-label="Close-up photo of a hand placing a polished steel calibration weight on a bench"></div>
  <div class="sq" style="left:204px;top:20px;width:41px;height:41px;background:rgba(190,30,45,.55)"></div>
  <div class="sq" style="left:176px;top:35px;width:26px;height:26px;background:rgba(200,80,90,.35)"></div>
  <div class="sq" style="left:204px;top:63px;width:41px;height:41px;background:rgba(230,140,90,.45)"></div>
  <div class="sq" style="left:244px;top:104px;width:22px;height:22px;background:rgba(230,120,40,.8)"></div>
  <div class="sq" style="left:44px;top:64px;width:157px;height:170px;background:rgba(220,100,40,.28)"></div>
  <div class="sq" style="left:0;top:223px;width:44px;height:40px;background:rgba(240,170,110,.5)"></div>
  <div class="sq" style="left:44px;top:223px;width:22px;height:22px;background:rgba(190,40,60,.7)"></div>
  <div class="sq" style="left:66px;top:246px;width:18px;height:18px;background:rgba(20,30,60,.7)"></div>
  <div class="cover-band"></div>
  <div class="brand-cover">HARBORLINE<br>WEIGHWORKS</div>
  <div class="cover-title">Lorem ipsum dolor sit amet, consectetur adipiscing elit</div>
  <div class="cover-sub">Lorem Ipsum is simply dummy text of the printing and typesetting industry. Lorem Ipsum has been the industry's</div>
  <div class="cover-url">harborlineweighworks.example</div>
</section>

<!-- Agenda -->
<section class="slide s-agenda">
  <svg class="frame" viewBox="0 0 514 289">
    <polygon points="350,60 400,60 290,289 240,289" fill="var(--faint)"/>
    <polyline points="19,41 444,41 470,0" fill="none" stroke="var(--navy)" stroke-width=".8"/>
    <polyline points="0,273 322,273 330,289" fill="none" stroke="var(--navy)" stroke-width=".6"/>
    <polygon points="404,273 514,273 514,289 410,289" fill="var(--navy)"/>
  </svg>
  <div class="slide-title">Lorem Ipsum is simply dummy text of the printing and typesetting industry.</div>
  <div class="brand-mini">Harborline Weighworks</div>
  <div class="item" style="left:55px;top:112px"><span class="num">01</span><span class="head">Lorem ipsum dolor</span><span class="sub">sed do eiusmod tempor incididunt</span></div>
  <div class="item" style="left:55px;top:148px"><span class="num">02</span><span class="head">Lorem ipsum dolor</span><span class="sub">sed do eiusmod tempor incididunt</span></div>
  <div class="item" style="left:55px;top:183px"><span class="num">03</span><span class="head">Lorem ipsum dolor</span><span class="sub">sed do eiusmod tempor incididunt</span></div>
  <div class="item" style="left:261px;top:112px"><span class="num">04</span><span class="head">onsectetur adipiscing elit</span><span class="sub">sed do eiusmod tempor incididunt</span></div>
  <div class="item" style="left:261px;top:148px"><span class="num">05</span><span class="head">onsectetur adipiscing elit</span><span class="sub">sed do eiusmod tempor incididunt</span></div>
  <div class="item" style="left:261px;top:183px"><span class="num">06</span><span class="head">onsectetur adipiscing elit</span><span class="sub">sed do eiusmod tempor incididunt</span></div>
  <div class="footnote">Lorem Ipsum is simply dummy text of the printing and typesetting industry. Lorem Ipsum has been the industry's</div>
  <div class="page-no">9</div>
</section>

<!-- Donut -->
<section class="slide s-donut">
  <svg class="frame" viewBox="0 0 514 289">
    <polygon points="350,60 400,60 290,289 240,289" fill="var(--faint)"/>
    <polyline points="19,41 444,41 470,0" fill="none" stroke="var(--navy)" stroke-width=".8"/>
    <polyline points="0,273 322,273 330,289" fill="none" stroke="var(--navy)" stroke-width=".6"/>
    <polygon points="404,273 514,273 514,289 410,289" fill="var(--navy)"/>
  </svg>
  <div class="slide-title">Lorem Ipsum is simply dummy text of the printing and typesetting industry.</div>
  <div class="brand-mini">Harborline Weighworks</div>

  <div class="pill" style="left:43px;top:91px"></div>
  <div class="pill" style="left:43px;top:160px"></div>
  <div class="pill" style="left:299px;top:91px"></div>
  <div class="pill" style="left:299px;top:160px"></div>

  <svg class="frame" viewBox="0 0 514 289">
    <circle cx="245" cy="144" r="60.5" fill="#fff"/>
    <path d="M245 73 A71 71 0 0 1 316 144 L295 144 A50 50 0 0 0 245 94 Z" fill="var(--orange-deep)"/>
    <path d="M316 144 A71 71 0 0 1 245 215 L245 194 A50 50 0 0 0 295 144 Z" fill="var(--green)"/>
    <path d="M245 215 A71 71 0 0 1 174 144 L195 144 A50 50 0 0 0 245 194 Z" fill="var(--blue)"/>
    <path d="M174 144 A71 71 0 0 1 245 73 L245 94 A50 50 0 0 0 195 144 Z" fill="var(--teal)"/>
    <g fill="none" stroke="#1f3a5f" stroke-width=".8">
      <path d="M237 131 l6 -4 h6 l4 3 M235 128 l2 5 6 0"/>
      <path d="M240 118 l1.5 3 3 .4 -2.2 2 .6 3 -2.9 -1.5 -2.9 1.5 .6 -3 -2.2 -2 3 -.4Z"/>
      <path d="M249 116 l1.2 2.4 2.5 .3 -1.8 1.7 .5 2.5 -2.4 -1.3 -2.4 1.3 .5 -2.5 -1.8 -1.7 2.5 -.3Z"/>
    </g>
    <circle cx="60.5" cy="108.5" r="17.5" fill="var(--teal)"/>
    <circle cx="60.5" cy="177.5" r="17.5" fill="var(--blue)"/>
    <circle cx="441.5" cy="108.5" r="17.5" fill="var(--orange-deep)"/>
    <circle cx="441.5" cy="177.5" r="17.5" fill="var(--green)"/>
    <g fill="none" stroke="#fff" stroke-width="1">
      <rect x="54" y="104" width="13" height="8"/><path d="M57 110v-3M60 110v-4M63 110v-2"/>
      <circle cx="60" cy="178" r="5"/><circle cx="60" cy="178" r="2"/><path d="M60 178 l6 -6"/>
      <circle cx="441.5" cy="104" r="2"/><circle cx="437.5" cy="111" r="1.8"/><circle cx="445.5" cy="111" r="1.8"/>
      <circle cx="440" cy="177" r="5"/><circle cx="444" cy="180" r="3" fill="var(--green)"/>
    </g>
  </svg>
  <div class="donut-label">Lorem Ipsum is simply dummy text of the printing and</div>
  <div class="pill-text" style="left:83px;top:96px">Lorem Ipsum is simply dummy text of the printing and typesetting industry. Lorem Ipsum has been the industry's</div>
  <div class="pill-text" style="left:86px;top:162px">Lorem Ipsum is simply dummy text of the printing and typesetting industry. Lorem Ipsum has been the industry's</div>
  <div class="pill-text" style="left:319px;top:96px">Lorem Ipsum is simply dummy text of the printing and typesetting industry. Lorem Ipsum has been the industry's</div>
  <div class="pill-text" style="left:319px;top:165px;width:106px">Lorem Ipsum is simply dummy text of the printing and typesetting industry. Lorem Ipsum has been the industry's</div>
  <div class="footnote">Lorem Ipsum is simply dummy text of the printing and typesetting industry. Lorem Ipsum has been the industry's</div>
  <div class="page-no">9</div>
</section>

<!-- Text and image -->
<section class="slide s-text">
  <svg class="frame" viewBox="0 0 514 289">
    <polygon points="350,60 400,60 290,289 240,289" fill="var(--faint)"/>
    <polyline points="19,41 444,41 470,0" fill="none" stroke="var(--navy)" stroke-width=".8"/>
    <polyline points="0,273 322,273 330,289" fill="none" stroke="var(--navy)" stroke-width=".6"/>
    <polygon points="404,273 514,273 514,289 410,289" fill="var(--navy)"/>
  </svg>
  <div class="slide-title">Lorem Ipsum is simply dummy text of the printing and typesetting industry.</div>
  <div class="brand-mini">Harborline Weighworks</div>
  <p class="body-copy">Lorem Ipsum is simply dummy text of the printing and typesetting industry. Lorem Ipsum has been the industry's standard dummy text ever since 1966, when designers at Typeline and Jonah Marsh, the librarian at Fleetwell Print Library in London, took a 1914 Cicero translation and scrambled it to make dummy text for Typeline's Body Type sheets. It has survived not only many decades, but also the leap into electronic typesetting, remaining essentially unchanged. It was popularised thanks to these sheets and more recently with desktop publishing software like PageSmith and WordDesk including versions of Lorem Ipsum.</p>
  <div class="photo-caliper" role="img" aria-label="Blue-toned photo of a digital caliper measuring a machined steel part"></div>
  <div class="footnote">Lorem Ipsum is simply dummy text of the printing and typesetting industry. Lorem Ipsum has been the industry's</div>
  <div class="page-no">9</div>
</section>

<!-- Process -->
<section class="slide s-process">
  <svg class="frame" viewBox="0 0 514 289">
    <defs>
      <radialGradient id="disc" cx="40%" cy="35%" r="70%">
        <stop offset="0" stop-color="#fafafa"/><stop offset="1" stop-color="#dcdcdc"/>
      </radialGradient>
    </defs>
    <polygon points="350,60 400,60 290,289 240,289" fill="var(--faint)"/>
    <polyline points="19,41 444,41 470,0" fill="none" stroke="var(--navy)" stroke-width=".8"/>
    <polyline points="0,273 322,273 330,289" fill="none" stroke="var(--navy)" stroke-width=".6"/>
    <polygon points="404,273 514,273 514,289 410,289" fill="var(--navy)"/>

    <path d="M73.5 153 A43.5 43.5 0 0 1 160.5 153 A43.5 43.5 0 0 0 247.5 153 A43.5 43.5 0 0 1 333.5 153 A43.5 43.5 0 0 0 420.5 153" fill="none" stroke="#333" stroke-width=".6" stroke-dasharray="2 1.5"/>
    <g fill="none" stroke="var(--orange-deep)" stroke-width="9" stroke-linecap="round">
      <path d="M86 121 A43.5 43.5 0 0 1 148 121"/>
      <path d="M172 185 A43.5 43.5 0 0 0 234 185"/>
      <path d="M259 121 A43.5 43.5 0 0 1 321 121"/>
      <path d="M346 185 A43.5 43.5 0 0 0 408 185"/>
    </g>
    <g fill="none" stroke="#fff" stroke-width=".6" stroke-dasharray="2 1.5">
      <path d="M86 121 A43.5 43.5 0 0 1 148 121"/>
      <path d="M172 185 A43.5 43.5 0 0 0 234 185"/>
      <path d="M259 121 A43.5 43.5 0 0 1 321 121"/>
      <path d="M346 185 A43.5 43.5 0 0 0 408 185"/>
    </g>
    <g fill="#fff" stroke="#222" stroke-width=".8">
      <circle cx="117" cy="109.5" r="3"/><circle cx="203" cy="196.5" r="3"/>
      <circle cx="290" cy="109.5" r="3"/><circle cx="377" cy="196.5" r="3"/>
    </g>
    <g fill="#222"><circle cx="117" cy="109.5" r="1.2"/><circle cx="203" cy="196.5" r="1.2"/><circle cx="290" cy="109.5" r="1.2"/><circle cx="377" cy="196.5" r="1.2"/></g>

    <circle cx="117" cy="153" r="30" fill="url(#disc)"/>
    <circle cx="203" cy="153" r="30" fill="url(#disc)"/>
    <circle cx="290" cy="153" r="30" fill="url(#disc)"/>
    <circle cx="377" cy="153" r="30" fill="url(#disc)"/>

    <g fill="none" stroke="#555" stroke-width=".8">
      <circle cx="120" cy="150" r="4"/><circle cx="120" cy="150" r="1.5"/>
      <circle cx="113" cy="157" r="3"/><circle cx="113" cy="157" r="1"/>
      <circle cx="203" cy="149" r="5"/><path d="M200.5 154 v4 h5 v-4 M201 160 h4 M203 140v-2 M195 149h-2 M211 149h2 M197 143l-1.5-1.5 M209 143l1.5-1.5"/>
      <path d="M282 144 v18 h17 M285 160 v-5 h2 v5 M289 160 v-9 h2 v9 M293 160 v-12 h2 v12"/>
      <circle cx="377" cy="148" r="2.5"/><circle cx="370" cy="150" r="2"/><circle cx="384" cy="150" r="2"/>
      <path d="M372 158 a5 5 0 0 1 10 0 M366 157 a4 4 0 0 1 6 -2.5 M388 157 a4 4 0 0 0 -6 -2.5"/>
    </g>
  </svg>
  <div class="slide-title">Lorem Ipsum is simply dummy text of the printing and typesetting industry.</div>
  <div class="brand-mini">Harborline Weighworks</div>
  <div class="step-title" style="left:153px;top:74px">Edit Title Here</div>
  <div class="step-text" style="left:153px;top:86px">This is a sample text. Insert your desired text here.</div>
  <div class="step-title" style="left:327px;top:74px">Edit Title Here</div>
  <div class="step-text" style="left:327px;top:86px">This is a sample text. Insert your desired text here.</div>
  <div class="step-title" style="left:67px;top:205px">Edit Title Here</div>
  <div class="step-text" style="left:67px;top:217px">This is a sample text. Insert your desired text here.</div>
  <div class="step-title" style="left:240px;top:205px">Edit Title Here</div>
  <div class="step-text" style="left:240px;top:217px">This is a sample text. Insert your desired text here.</div>
  <div class="footnote">Lorem Ipsum is simply dummy text of the printing and typesetting industry. Lorem Ipsum has been the industry's</div>
  <div class="page-no">9</div>
</section>

<!-- Closing -->
<section class="slide s-close">
  <div class="close-photo" role="img" aria-label="Soft light-blue photo of two business people shaking hands"></div>
  <div class="close-left"></div>
  <svg class="frame" viewBox="0 0 514 289">
    <polygon points="0,0 22,0 0,22" fill="#b07a45"/>
    <rect x="462" y="17" width="33" height="33" fill="#f0a865" opacity=".85"/>
    <rect x="451" y="39" width="21" height="21" fill="#d9363e" opacity=".8"/>
  </svg>
  <div class="brand-close">HARBORLINE<br>WEIGHWORKS</div>
  <div class="cta">
    <div class="cta-head">Ready to<br>Work With Us?</div>
    <div class="cta-link" style="top:85px">www.harborlineweighworks.example</div>
    <div class="cta-link" style="top:100px">info@harborlineweighworks.example</div>
  </div>
  <div class="thanks">Thank You!</div>
</section>

</body>
</html>
```